Dentistry

Dentist's personal business card. No logo needed. The card shoul deliver the massage of reliability, professionalism, experience.
Please ad the full brief of the project: down the line it says: the winning look should be precise and pristine NO pictures of Teeth, smiles, instruments etc.

The details to be desplaid are:
Dr. Rob Valdoni
Doctor of Dental Surgery
PHD
Web. Www.drvaldoni.com
Email. Rob@drvaldoni.com
Tel 07731482590
Surgery address. 27Bharwick road London SW4 7QN UK
82 Fenwyn Row London SW3 2HT. Uk

Reason: Decided to make the payment unrefundable in order to get more designers involved.

Requirements
Should not have
• Logo, teeth, smile any sort of instruments.

```html
<!DOCTYPE html>
<html lang="en">
<head>
<meta charset="utf-8">
<title>Dr. Rob Valdoni – Business Card</title>
<link href="https://fonts.googleapis.com/css2?family=Tinos&family=Marcellus&family=Cormorant+Garamond:wght@500&display=swap" rel="stylesheet">
<style>
  :root {
    --page: #ececec;
    --white: #ffffff;
    --ink: #111111;
    --green-light: #2bb673;
    --green-dark: #08693a;
    --shadow: rgba(0, 0, 0, 0.18);
  }
  * { box-sizing: border-box; margin: 0; padding: 0; }
  html, body {
    width: 1200px;
    height: 1200px;
    overflow: hidden;
    background: var(--page);
  }
  .canvas {
    width: 1200px;
    height: 1200px;
    display: flex;
    flex-direction: column;
    align-items: center;
    justify-content: center;
    gap: 40px;
  }
  .card {
    position: relative;
    width: 1000px;
    height: 540px;
    border-radius: 34px;
    overflow: hidden;
    box-shadow: 0 8px 24px var(--shadow);
  }
  .card-front { background: var(--white); }
  .card-front .swoosh {
    position: absolute;
    inset: 0;
    width: 100%;
    height: 100%;
  }
  .identity {
    position: absolute;
    top: 80px;
    left: 300px;
    color: var(--ink);
    font-family: "Tinos", "Times New Roman", serif;
    transform: rotate(-4deg);
    transform-origin: left top;
  }
  .identity .name {
    font-size: 80px;
    line-height: 1;
    white-space: nowrap;
  }
  .identity .degree {
    font-family: "Cormorant Garamond", "Times New Roman", serif;
    font-weight: 500;
    font-size: 50px;
    line-height: 1.05;
    margin-left: 70px;
    white-space: nowrap;
  }
  .identity .title {
    font-size: 46px;
    line-height: 1.1;
    margin-left: 370px;
  }
  .card-back {
    background: var(--green-light);
    color: var(--white);
  }
  .contact {
    position: absolute;
    top: 130px;
    right: 235px;
    text-align: right;
    font-family: "Marcellus", "Times New Roman", serif;
    font-size: 50px;
    line-height: 1.12;
  }
  .contact .tel {
    letter-spacing: 4px;
    font-family: "Tinos", "Times New Roman", serif;
    font-size: 48px;
  }
  .address {
    position: absolute;
    top: 350px;
    right: 100px;
    text-align: right;
    font-family: "Cormorant Garamond", "Times New Roman", serif;
    font-weight: 500;
    font-size: 40px;
    line-height: 1.3;
  }
</style>
</head>
<body>
<main class="canvas">
  <section class="card card-front">
    <svg class="swoosh" viewBox="0 0 1000 540" preserveAspectRatio="none" aria-hidden="true">
      <path d="M0 370 C 320 350, 760 300, 1000 120 L1000 540 L0 540 Z" fill="var(--green-light)"/>
      <path d="M0 395 C 330 378, 770 330, 1000 185 L1000 540 L0 540 Z" fill="var(--green-dark)"/>
    </svg>
    <div class="identity">
      <p class="name">Dr. Rob Valdoni</p>
      <p class="degree">Doctor of Dental Surgery</p>
      <p class="title">PHD</p>
    </div>
  </section>

  <section class="card card-back">
    <div class="contact">
      <p class="web">Web. Www.drvaldoni.com</p>
      <p class="email">Email. Rob@drvaldoni.com</p>
      <p class="tel">Tel 07731482590</p>
    </div>
    <div class="address">
      <p>Surgery address. 27Bharwick road London SW4 7QN UK</p>
      <p>82 Fenwyn Row London SW3 2HT. Uk</p>
    </div>
  </section>
</main>
</body>
</html>
```